Redfield interiors PTY LTD

My business specializes in commercial fitout which builds walls, ceilings, doors, uses also materials aluminium in works. Id like to have a logo designed for my company too.

Industry/Entity Type

Business

```html
<!DOCTYPE html>
<html lang="en">
<head>
<meta charset="utf-8">
<title>Redfield Interiors PTY LTD — Business Card</title>
<link rel="stylesheet" href="https://fonts.googleapis.com/css2?family=Arimo:wght@400;700&display=swap">
<style>
  :root {
    --stage: #2a2a2d;
    --front-top: #0673ba;
    --front-bottom: #2c3479;
    --white: #ffffff;
    --navy: #25408f;
    --blue-line: #1e6aa8;
    --role-blue: #1d4e9e;
    --grey-text: #7d7d7d;
    --name-grey: #8a8a8a;
    --faint-ring-front: rgba(255,255,255,0.12);
    --faint-ring-back: #eceef6;
  }
  * { box-sizing: border-box; margin: 0; padding: 0; }
  html, body {
    width: 1189px; height: 1200px; overflow: hidden;
    background: var(--stage);
    font-family: "Arimo", Arial, sans-serif;
  }
  .card {
    position: absolute; left: 171px; width: 856px; height: 488px;
    border-radius: 26px; overflow: hidden;
  }
  .card--front {
    top: 67px;
    background: linear-gradient(180deg, var(--front-top) 0%, var(--front-bottom) 100%);
  }
  .card--back { top: 625px; background: var(--white); }
  .deco-ring { position: absolute; border-radius: 50%; }
  .card--front .deco-ring {
    left: -107px; top: -2px; width: 490px; height: 490px;
    border: 5px solid var(--faint-ring-front);
  }
  .card--back .deco-ring {
    left: 519px; top: -9px; width: 384px; height: 384px;
    border: 6px solid var(--faint-ring-back);
  }
  .brand-dot { position: absolute; border-radius: 50%; width: 118px; height: 118px; }
  .card--front .brand-dot { left: 186px; top: 183px; border: 3px solid var(--white); }
  .card--back .brand-dot { left: 48px; top: 67px; border: 3px solid var(--navy); }
  .wordmark {
    position: absolute; font-weight: 700; text-transform: uppercase; line-height: 1;
  }
  .wordmark__name { display: block; font-size: 47px; letter-spacing: 0.13em; }
  .wordmark__sub { display: block; font-size: 22px; letter-spacing: 0.30em; margin-top: 8px; }
  .card--front .wordmark { left: 335px; top: 212px; color: var(--white); }
  .card--back .wordmark { left: 198px; top: 96px; color: var(--navy); }
  .front-url {
    position: absolute; left: 0; right: 0; top: 410px; text-align: center;
    color: var(--white); font-size: 21px; letter-spacing: 0.52em;
  }
  .person { position: absolute; left: 47px; top: 290px; line-height: 1; }
  .person__name { font-weight: 700; font-size: 27px; color: var(--name-grey); }
  .person__role { font-size: 23px; color: var(--role-blue); margin-top: 1px; }
  .divider {
    position: absolute; left: 47px; width: 766px; top: 350px;
    height: 2px; background: var(--blue-line);
  }
  .contacts { position: absolute; left: 46px; top: 372px; list-style: none; }
  .contacts li {
    display: flex; align-items: center; height: 28px;
    font-size: 21px; color: var(--grey-text);
  }
  .contacts svg { width: 24px; height: 24px; margin-right: 11px; flex: none; }
  .address {
    position: absolute; right: 43px; top: 393px; text-align: right;
    font-size: 21px; line-height: 27px; color: var(--grey-text);
  }
</style>
</head>
<body>
  <section class="card card--front">
    <div class="deco-ring"></div>
    <div class="brand-dot"></div>
    <div class="wordmark">
      <span class="wordmark__name">Redfield</span>
      <span class="wordmark__sub">Interiors PTY LTD</span>
    </div>
    <p class="front-url">www.redfieldfitout.com</p>
  </section>

  <section class="card card--back">
    <div class="deco-ring"></div>
    <div class="brand-dot"></div>
    <div class="wordmark">
      <span class="wordmark__name">Redfield</span>
      <span class="wordmark__sub">Interiors PTY LTD</span>
    </div>

    <div class="person">
      <p class="person__name">NORA CASTELL</p>
      <p class="person__role">Founder</p>
    </div>
    <div class="divider"></div>

    <ul class="contacts">
      <li>
        <svg viewBox="0 0 24 24" aria-hidden="true">
          <circle cx="12" cy="12" r="11" fill="none" stroke="#25408f" stroke-width="1.6"/>
          <path d="M7 10 Q12 6 17 10 L15.5 11.5 L13.5 10.5 L10.5 10.5 L8.5 11.5 Z M8.5 12.5 H15.5 V16.5 H8.5 Z" fill="#25408f"/>
        </svg>
        (031) 582-4417
      </li>
      <li>
        <svg viewBox="0 0 24 24" aria-hidden="true">
          <circle cx="12" cy="12" r="11" fill="none" stroke="#25408f" stroke-width="1.6"/>
          <rect x="6.5" y="8" width="11" height="8" fill="#25408f"/>
          <path d="M6.5 8 L12 12.5 L17.5 8" fill="none" stroke="#fff" stroke-width="1.2"/>
        </svg>
        hello@redfieldfitout.com
      </li>
      <li>
        <svg viewBox="0 0 24 24" aria-hidden="true">
          <circle cx="12" cy="12" r="11" fill="none" stroke="#25408f" stroke-width="1.6"/>
          <circle cx="12" cy="12" r="6.5" fill="none" stroke="#25408f" stroke-width="1.3"/>
          <ellipse cx="12" cy="12" rx="2.8" ry="6.5" fill="none" stroke="#25408f" stroke-width="1.1"/>
          <path d="M5.5 12 H18.5 M6.5 9 H17.5 M6.5 15 H17.5" stroke="#25408f" stroke-width="1"/>
        </svg>
        www.redfieldfitout.com
      </li>
    </ul>

    <address class="address" style="font-style: normal;">
      PO BOX 408 Ardmore Lane<br>
      5th street Kelvale
    </address>
  </section>
</body>
</html>
```